Flyer Mail out

Need something urgently designed.

I need a flyer done double sided I have provided KTHS photos and the writing. I do not have any dental surgery stock photos as such but this can be used. We are a mobile dental company that goes out to schools and provide free dental services.

I have attached the written document and would like it double sided A4 paper.

The colours I want is Aqua, Light Blue, dark blue, grey and white.

Just need it designed beautifully and professionally to go out to principals to contact us and use our services.

If you would like more info have a look at our Facebook page Kestrel Travelling Health Smiles

```html
<!DOCTYPE html>
<html lang="en">
<head>
<meta charset="utf-8">
<title>KTHS Flyer – Front and Back</title>
<link rel="stylesheet" href="https://fonts.googleapis.com/css2?family=Nunito:ital,wght@0,400;0,600;0,700;0,800;0,900;1,700&display=swap">
<style>
:root{
  --blue:#1c78c0;
  --blue-deep:#0f5c9e;
  --blue-soft:#5aa6dc;
  --sky:#d9ebf7;
  --mist:#eef4f9;
  --aqua:#17a398;
  --ink:#2f3a44;
  --grey:#8c969e;
  --white:#ffffff;
  --stage:#e6e8ea;
}
*{margin:0;padding:0;box-sizing:border-box}
html,body{width:1200px;height:1000px;overflow:hidden;background:var(--stage);font-family:"Nunito",Arial,sans-serif;color:var(--ink)}
.spread{position:relative;width:1200px;height:1000px}
.page{position:absolute;top:100px;width:566px;height:800px;background:var(--white);overflow:hidden;box-shadow:0 4px 18px rgba(0,0,0,.18)}
.page--front{left:20px}
.page--back{left:614px}
.page__bg{position:absolute;inset:0;width:566px;height:800px}
.headline{position:absolute;top:38px;left:0;width:100%;text-align:center;color:var(--white);font-weight:900;font-size:36px;line-height:38px;letter-spacing:.5px}
.stat{position:absolute;top:122px;left:48px;width:470px;text-align:center;color:var(--white);font-weight:800;font-size:16px;line-height:19px}
.stat small{font-size:12px;font-weight:700}
.lead{position:absolute;top:200px;left:50px;width:466px;text-align:center;color:var(--white);font-size:14px;line-height:18px}
.photo{position:absolute}
.photo--clinic{left:0;top:285px;width:130px;height:290px;background:linear-gradient(160deg,#f3f5f7,#cfd6dc 60%,#2a2a2e)}
.photo--team{left:130px;top:285px;width:250px;height:290px;background:linear-gradient(180deg,#c9d3dc,#e7ebef 40%,#55606e 75%,#8e98a2)}
.photo--treatment{left:380px;top:270px;width:186px;height:305px;background:linear-gradient(200deg,#e9e2dc,#c9b7a8 45%,#2d2f35 80%)}
.badge{position:absolute;width:168px;height:168px;border-radius:50%;background:radial-gradient(circle at 40% 35%,#ffffff,#e3ebf2);box-shadow:0 3px 10px rgba(0,0,0,.22);text-align:center;color:var(--aqua);font-weight:800;font-size:15.5px;line-height:18px;padding-top:30px}
.badge strong{display:block;color:var(--blue);font-size:18px;margin-top:6px}
.badge svg{display:block;margin:-4px auto 0}
.page--front .badge{left:318px;top:476px}
.page--back .badge{left:372px;top:500px}
.contact{position:absolute;left:40px;width:240px;font-size:11.5px;line-height:14px;color:var(--ink)}
.contact p{margin-bottom:8px}
.contact b{color:var(--aqua);font-weight:800}
.contact .fine{font-size:10px;line-height:12.5px;margin-bottom:0}
.page--front .contact{top:606px}
.page--back .contact{top:612px}
.truck{position:absolute;right:16px;width:240px;height:96px;border-radius:6px 6px 14px 14px;background:linear-gradient(180deg,#f4f6f8,#d7dde3 70%,#4b525a)}
.page--front .truck{top:690px}
.page--back .truck{top:690px}
.letter{position:absolute;top:30px;left:34px;width:498px;color:var(--white);font-size:9.8px;line-height:12.4px}
.letter h2{font-size:19px;font-weight:900;margin-bottom:8px}
.letter p{margin-bottom:7px}
.letter ul{list-style:none;margin:-2px 0 7px}
.letter li{font-weight:800;padding-left:9px;position:relative}
.letter li::before{content:"";position:absolute;left:0;top:4.5px;width:4px;height:4px;border-radius:50%;background:var(--white)}
.letter em{font-weight:800}
.sign{font-weight:800}
</style>
</head>
<body>
<main class="spread">

  <section class="page page--front">
    <div class="photo photo--clinic" role="img" aria-label="Smiling dental staff in a bright clinic"></div>
    <div class="photo photo--team" role="img" aria-label="Dental team standing in front of the mobile clinic truck"></div>
    <div class="photo photo--treatment" role="img" aria-label="Dentist treating a student in the dental chair"></div>
    <svg class="page__bg" viewBox="0 0 566 800" aria-hidden="true">
      <path d="M0 0H566V250Q330 330 0 290Z" fill="var(--blue-soft)" opacity=".55"/>
      <path d="M0 0H566V232Q320 318 0 272Z" fill="var(--blue)"/>
      <path d="M0 560Q180 600 566 548V800H0Z" fill="var(--sky)"/>
      <path d="M0 580Q220 610 566 566V800H0Z" fill="var(--mist)"/>
      <path d="M0 596Q240 620 566 584V800H0Z" fill="var(--white)"/>
    </svg>
    <h1 class="headline">OUR FOCUS IS ON<br>EDUCATION &amp; PREVENTION</h1>
    <p class="stat">1 in 5 children between the ages of 4-8 years of age will suffer from tooth decay or dental caries as a result of poor dental hygiene <small>(ref; Southern College of Child Health)</small></p>
    <p class="lead">Thus, leading to possible dental destruction to their adult teeth. This, in conjunction with diet, lifestyle and social welfare can be contribution to the increase of child absenteeism.</p>
    <div class="badge">Book us now for<br>2015 and help<br>us, bring back<br>your student's<strong>Bright Smile</strong>
      <svg width="110" height="14" viewBox="0 0 110 14"><path d="M4 2Q55 18 106 2" fill="none" stroke="var(--blue)" stroke-width="2.5" stroke-linecap="round"/></svg>
    </div>
    <div class="contact">
      <p>To find out about our procedures or to book your school for 2015 and take advantage of this opportunity, Please visit our website <b>www.kths.net.au</b> or email me at <b>mara.l@kths.net.au</b></p>
      <p>Or to speak to one of our friendly staff, call us directly on <b>(02) 5550 1234</b></p>
      <p class="fine">In addition, feel free to visit <b>our social pages</b> to see regular updates, features, special offers and daily tips regarding our services.</p>
    </div>
    <div class="truck" role="img" aria-label="White mobile dental clinic truck and trailer"></div>
  </section>

  <section class="page page--back">
    <svg class="page__bg" viewBox="0 0 566 800" aria-hidden="true">
      <path d="M0 0H566V548Q300 628 0 578Z" fill="var(--blue-soft)" opacity=".55"/>
      <path d="M0 0H566V528Q300 616 0 560Z" fill="var(--blue)"/>
      <path d="M0 588Q220 628 566 578V800H0Z" fill="var(--sky)"/>
      <path d="M0 604Q240 634 566 594V800H0Z" fill="var(--white)"/>
    </svg>
    <article class="letter">
      <h2>Dear Principal,</h2>
      <p>We thank you for the time you are taking to review our mobile dental service. Here at Kestrel Travelling Health Smiles (KTHS), we are committed to '<em>bringing the dentist to you</em>'.</p>
      <p>We are <em>passionate</em> about providing <em>Bulked Billed</em> Oral Health Care to Primary and High Schools, Aged Care Facilities, Corporate Companies and Aboriginal Communities.</p>
      <p>Within New South Wales, in the past year, we have serviced over 150 schools, and treated a total of 22,014 students so far.</p>
      <p>We are pleased to introduce our service designed to satisfy your student's dental needs. Our service is cost effective, user friendly and extremely beneficial in providing oral health <em>education</em> and <em>prevention</em>. We offer;</p>
      <ul>
        <li>Free Bulk-Billed assessment and treatment to students who qualify for HealthCover "Smile Start" program; this includes a dental check-up, cleaning &amp; fluoride treatment, sealants, X-rays and fillings.</li>
        <li>One-on-one Oral Health education from our professional dentists and oral health therapists</li>
        <li>Complimentary Dental Care Pack comprising of a toothbrush, toothpaste and other products</li>
        <li>Students also go into the draw to win various prices drawn after the clinic's visit to the school</li>
        <li>Provide a referral to the student's regular dentist for further treatment they may require</li>
      </ul>
      <p>KTHS operates within accepted best practice models, and as such, is familiar, and without exception complies with the relevant legislation, regulations, Codes and guidelines governing dentistry, including but not limited to, the Dental Code of Conduct for Health Practitioners by the National Dental Practice Board.</p>
      <p>Our mobile dental clinics feature state-of-the-art, oral health equipment and machinery. Including Dental X-Ray OPG that features low dose radiation, as well as <em>Child Safety Standard Wheel Chair Access</em>. (Please see our website for more information)</p>
      <p>Thank you for considering KTHS, my team and I look forward to providing this free service to your school and most importantly, '<em>bringing the dentist to you</em>'.</p>
      <p class="sign">Kind Regards,<br><br>Mara Lindqvist (signature)<br>Marketing Manager</p>
    </article>
    <div class="badge">Book us now for<br>2015 and help<br>us, bring back<br>your student's<strong>Bright Smile</strong>
      <svg width="110" height="14" viewBox="0 0 110 14"><path d="M4 2Q55 18 106 2" fill="none" stroke="var(--blue)" stroke-width="2.5" stroke-linecap="round"/></svg>
    </div>
    <div class="contact">
      <p>To find out about our procedures or to book your school for 2015 and take advantage of this opportunity, Please visit our website <b>www.kths.net.au</b> or email me at <b>mara.l@kths.net.au</b></p>
      <p>Or to speak to one of our friendly staff, call us directly on <b>(02) 5550 1234</b></p>
      <p class="fine">In addition, feel free to visit <b>our social pages</b> to see regular updates, features, special offers and daily tips regarding our services.</p>
    </div>
    <div class="truck" role="img" aria-label="White mobile dental clinic truck and trailer"></div>
  </section>

</main>
</body>
</html>
```